Service vs Service Timeline Design

We need a graphic designed to show the difference between our service and another service. We have a wireframe of the "timeline" between the services to give you an idea of what the graphic design will need to look like. You will have some creative ability to make it was better then the wireframe, that is titled "wireframe". There are pictures of our mobile app attached as well for you to get a feel for our design. If this graphic goes well, we have another graphic in the pipeline. Our website is: https://www.quoddle.com. We are in the process of building a website that better matches the design of our app right now.
It Service

```html
<!DOCTYPE html>
<html lang="en">
<head>
<meta charset="utf-8">
<title>Quoddle vs Disposal Bins – Removal Timeline</title>
<link href="https://fonts.googleapis.com/css2?family=Bebas+Neue&family=Roboto+Condensed:wght@400;700&display=swap" rel="stylesheet">
<style>
  :root{
    --blue:#4d80c4;
    --blue-deep:#1767b3;
    --blue-line:#2d5a92;
    --navy-ink:#1c2636;
    --grey-band:#c1c2c4;
    --grey-panel:#e6e7e8;
    --grey-line:#b9babc;
    --road:#333436;
    --diamond:#58595b;
    --ink:#2f3033;
    --white:#ffffff;
    --star:#ffe33b;
    --happy:#4fbf45;
    --angry:#e9542b;
  }
  *{box-sizing:border-box;margin:0;padding:0}
  html,body{width:1000px;height:1200px;overflow:hidden;background:var(--white)}
  body{position:relative;font-family:"Roboto Condensed",Arial Narrow,sans-serif}

  .header-band{position:absolute;top:0;left:0}
  .band-title{position:absolute;top:66px;font-family:"Bebas Neue",Impact,sans-serif;font-size:66px;line-height:72px;letter-spacing:1px;color:var(--white)}
  .band-title--left{left:90px;width:360px;text-align:center}
  .band-title--right{left:560px;width:360px;text-align:center}

  .road{position:absolute;left:468px;top:150px;width:64px;height:983px;background:var(--road)}
  .road::after{content:"";position:absolute;left:31px;top:38px;bottom:0;border-left:2px dashed var(--white)}

  .panel{position:absolute;top:200px;width:401px}
  .panel--ours{left:67px;height:763px;background:var(--blue);border-radius:30px 0 0 30px}
  .panel--theirs{left:532px;height:933px;background:var(--grey-panel);border-radius:0 30px 30px 0}

  .step{position:absolute;left:0;width:401px;display:grid;align-items:center}
  .panel--ours .step{grid-template-columns:34px 1fr 110px;column-gap:14px;padding:0 10px 0 36px}
  .panel--theirs .step{grid-template-columns:96px 1fr 36px;column-gap:28px;padding:0 38px 0 18px}

  .step-text{font-weight:700;font-size:21px;line-height:26px}
  .panel--ours .step-text{color:var(--white);text-align:right}
  .panel--theirs .step-text{color:var(--ink);font-weight:400;-webkit-text-stroke:.4px var(--ink)}
  .step-text sup{font-size:11px}

  .divider{position:absolute;height:1px}
  .panel--ours .divider{left:29px;right:0;background:var(--blue-line)}
  .panel--ours .divider::before{content:"";position:absolute;left:-2px;top:-2px;width:5px;height:5px;border-radius:50%;background:var(--navy-ink)}
  .panel--theirs .divider{left:0;width:356px;background:var(--grey-line)}
  .panel--theirs .divider::after{content:"";position:absolute;right:-2px;top:-2px;width:5px;height:5px;border-radius:50%;background:var(--grey-line)}

  .date{width:34px;height:34px;background:var(--white);border-radius:3px;box-shadow:2px 2px 3px rgba(0,0,0,.35);text-align:center;overflow:hidden;justify-self:start}
  .panel--theirs .date{justify-self:end}
  .date-month{display:block;background:var(--navy-ink);color:var(--white);font-size:7px;font-weight:700;line-height:10px}
  .date-day{display:block;color:var(--navy-ink);font-weight:700;font-size:18px;line-height:23px}
  .date-day sup{font-size:8px}
  .date-day--range{font-size:13px}

  .art{display:block;border-radius:6px}
  .panel--ours .art{background:var(--navy-ink)}
  .panel--theirs .art{background:#3a3a3c}

  .summary{position:absolute;color:var(--white);text-align:center;border-radius:12px}
  .summary--ours{left:77px;top:600px;width:188px;height:128px;background:var(--blue-deep);border-bottom-right-radius:0}
  .summary--ours::after{content:"";position:absolute;right:-10px;bottom:0;border-left:10px solid var(--blue-deep);border-top:12px solid transparent}
  .summary--theirs{left:136px;top:756px;width:156px;height:128px;background:var(--blue);border-bottom-left-radius:0}
  .summary--theirs::after{content:"";position:absolute;left:-10px;bottom:0;border-right:10px solid var(--blue);border-top:12px solid transparent}
  .summary-label{font-size:15px;line-height:18px;padding-top:14px}
  .summary-mood{display:flex;justify-content:center;align-items:center;gap:8px;height:44px;margin-top:2px}
  .star{color:var(--star);font-size:16px}
  .mood{width:38px;height:38px;border-radius:50%}
  .mood--happy{background:var(--happy)}
  .mood--angry{background:var(--angry)}
  .summary-value{font-family:Arial,Helvetica,sans-serif;font-weight:700;font-size:32px;line-height:38px}
</style>
</head>
<body>

<svg class="header-band" width="1000" height="220" viewBox="0 0 1000 220" aria-hidden="true">
  <polygon points="67,64 480,64 480,137 67,137 95,100" fill="#4d80c4"/>
  <polygon points="520,64 933,64 905,100 933,137 520,137" fill="#c1c2c4"/>
  <polygon points="500,34 572,100 500,170 428,100" fill="#ffffff"/>
  <polygon points="500,44 562,100 500,160 438,100" fill="#58595b"/>
  <text x="500" y="118" text-anchor="middle" font-family="Bebas Neue, Impact, sans-serif" font-size="54" fill="#ffffff">V/S</text>
</svg>
<div class="band-title band-title--left">Quoddle</div>
<div class="band-title band-title--right">Disposal Bins</div>

<div class="road" aria-hidden="true"></div>

<section class="panel panel--ours" aria-label="Quoddle timeline">
  <div class="step" style="top:0;height:114px">
    <div class="date"><span class="date-month">APRIL</span><span class="date-day">1<sup>st</sup></span></div>
    <p class="step-text">Order Anywhere,<br>Order Anytime</p>
    <span class="art" role="img" aria-label="Hand holding a phone with a map" style="width:64px;height:96px;justify-self:center"></span>
  </div>
  <div class="divider" style="top:114px"></div>

  <div class="step" style="top:114px;height:134px">
    <div class="date"><span class="date-month">APRIL</span><span class="date-day">2<sup>nd</sup></span></div>
    <p class="step-text">Quoddle Removal<br>Partners on the<br>way with real-time<br>status updates</p>
    <span class="art" role="img" aria-label="Trucks driving to map pins" style="width:120px;height:72px;opacity:.55"></span>
  </div>
  <div class="divider" style="top:248px"></div>

  <div class="step" style="top:248px;height:106px">
    <div class="date"><span class="date-month">APRIL</span><span class="date-day">2<sup>nd</sup></span></div>
    <p class="step-text">Quoddle Removal<br>Partners load the<br>trailer quickly</p>
    <span class="art" role="img" aria-label="Worker pushing a loaded hand truck" style="width:80px;height:80px;justify-self:center"></span>
  </div>
  <div class="divider" style="top:354px"></div>

  <div class="step" style="top:354px;height:88px">
    <div class="date"><span class="date-month">APRIL</span><span class="date-day">2<sup>nd</sup></span></div>
    <p class="step-text">Junk Gone<br>Faster</p>
    <span class="art" role="img" aria-label="Worker waving off a truck with a trailer" style="width:124px;height:52px;opacity:.7"></span>
  </div>
  <div class="divider" style="top:442px"></div>

  <div class="step" style="top:442px;height:136px">
    <div class="date"><span class="date-month">APRIL</span><span class="date-day">2<sup>nd</sup></span></div>
    <p class="step-text">Feedback is easy.<br>Fast Improvements.<br>Instantly know<br>best workers.</p>
    <svg width="86" height="92" viewBox="0 0 86 92" role="img" aria-label="Shield with a tick" style="justify-self:center">
      <path d="M43 4 C30 14 16 16 6 16 C6 52 20 76 43 88 C66 76 80 52 80 16 C70 16 56 14 43 4 Z" fill="#1c2636"/>
      <path d="M43 14 C33 21 23 24 15 24 C16 52 27 70 43 79 C59 70 70 52 71 24 C63 24 53 21 43 14 Z" fill="#4d80c4"/>
      <path d="M24 46 L38 62 L78 18 L82 22 L38 72 L18 50 Z" fill="#ffffff" stroke="#1c2636" stroke-width="3"/>
    </svg>
  </div>

  <div class="summary summary--ours">
    <p class="summary-label">Total Removal Time Line</p>
    <div class="summary-mood"><span class="star">★</span><span class="star">★</span><span class="mood mood--happy" role="img" aria-label="Happy face"></span><span class="star">★</span><span class="star">★</span></div>
    <p class="summary-value">1-3 Hours</p>
  </div>
</section>

<section class="panel panel--theirs" aria-label="Disposal bins timeline">
  <div class="step" style="top:0;height:130px">
    <span class="art" role="img" aria-label="Computer monitor and telephone" style="width:96px;height:80px"></span>
    <p class="step-text">Order Online<br>or Call</p>
    <div class="date"><span class="date-month">APRIL</span><span class="date-day">1<sup>st</sup></span></div>
  </div>
  <div class="divider" style="top:130px"></div>

  <div class="step" style="top:130px;height:95px">
    <span class="art" role="img" aria-label="Person relaxing in a chair" style="width:80px;height:60px"></span>
    <p class="step-text">“We will drop<br>it on the 7<sup>th</sup> ”</p>
    <div class="date"><span class="date-month">APRIL</span><span class="date-day">7<sup>th</sup></span></div>
  </div>
  <div class="divider" style="top:225px"></div>

  <div class="step" style="top:225px;height:114px">
    <span class="art" role="img" aria-label="Empty disposal bin" style="width:80px;height:50px"></span>
    <p class="step-text">Disposal Bin<br>arrives on the<br>Apr 8<sup>th</sup></p>
    <div class="date"><span class="date-month">APRIL</span><span class="date-day">8<sup>th</sup></span></div>
  </div>
  <div class="divider" style="top:339px"></div>

  <div class="step" style="top:339px;height:90px">
    <span class="art" role="img" aria-label="Person loading a disposal bin with a hand truck" style="width:110px;height:66px"></span>
    <p class="step-text">"You load bin for<br>a week”</p>
    <div class="date"><span class="date-month">APRIL</span><span class="date-day date-day--range">8<sup>to</sup>15</span></div>
  </div>
  <div class="divider" style="top:429px"></div>

  <div class="step" style="top:429px;height:89px">
    <svg width="96" height="70" viewBox="0 0 96 70" role="img" aria-label="Ringing telephone" style="justify-self:center">
      <path d="M14 24 C20 10 60 10 66 24 L58 32 L50 26 L50 20 C44 18 36 18 30 20 L30 26 L22 32 Z" fill="#2e2e2e"/>
      <path d="M24 34 L56 34 L64 62 L16 62 Z" fill="#2e2e2e"/>
      <circle cx="40" cy="47" r="8" fill="#e6e7e8"/>
      <circle cx="40" cy="47" r="3" fill="#2e2e2e"/>
      <path d="M70 8 Q78 14 76 24" stroke="#2e2e2e" stroke-width="4" fill="none" stroke-linecap="round"/>
      <path d="M78 2 Q90 12 86 28" stroke="#2e2e2e" stroke-width="4" fill="none" stroke-linecap="round"/>
    </svg>
    <p class="step-text">Call to have<br>bin picked up</p>
    <div class="date"><span class="date-month">APRIL</span><span class="date-day">14<sup>th</sup></span></div>
  </div>
  <div class="divider" style="top:518px"></div>

  <div class="step" style="top:518px;height:88px">
    <span class="art" role="img" aria-label="Full disposal bin beside a worker" style="width:90px;height:62px"></span>
    <p class="step-text">Pickup bin<br>on the15<sup>th</sup></p>
    <div class="date"><span class="date-month">APRIL</span><span class="date-day">15<sup>th</sup></span></div>
  </div>
  <div class="divider" style="top:606px"></div>

  <div class="step" style="top:606px;height:140px;grid-template-columns:96px 1fr 36px;column-gap:28px">
    <svg width="86" height="92" viewBox="0 0 86 92" role="img" aria-label="Shield with a cross" style="justify-self:center">
      <path d="M43 4 C30 14 16 16 6 16 C6 52 20 76 43 88 C66 76 80 52 80 16 C70 16 56 14 43 4 Z" fill="#2e2e2e"/>
      <path d="M43 14 C33 21 23 24 15 24 C16 52 27 70 43 79 C59 70 70 52 71 24 C63 24 53 21 43 14 Z" fill="#e6e7e8"/>
      <path d="M30 30 L46 46 L72 18 L78 24 L52 52 L68 70 L62 76 L46 58 L30 76 L24 70 L40 52 L24 36 Z" fill="#ffffff" stroke="#2e2e2e" stroke-width="3"/>
    </svg>
    <p class="step-text" style="margin-right:-60px">No easy feedback method.<br>Slow Improvements<br>Months to guess<br>best workers</p>
    <div class="date"><span class="date-month">?</span><span class="date-day">?</span></div>
  </div>

  <div class="summary summary--theirs">
    <p class="summary-label">Total Removal Time Line</p>
    <div class="summary-mood"><span class="mood mood--angry" role="img" aria-label="Angry face"></span></div>
    <p class="summary-value">2 Weeks</p>
  </div>
</section>

</body>
</html>
```